Etiketten für Rotwein
Zielgruppe
Wir starten dieses Jahr mit unserem ersten Rotwein unserer neuen Marke CAL VERDUNES aus unserem neuen Weingut auf Mallorca.
Es folgen in den kommenden Jahren ein Rosé und weitere Weißweine.
Aufgabenstellung
Wir suchen ein Design für unser erstes Flaschenetikett der Rotweinflaschen.
Die Höhe soll maximal 130 mm sein.
Der Name soll 'Bertoldo' sein.
Die Rebsorte 'Cabernet Sauvignon' und der Jahrgang '2025' sollen mit erscheinen.
Unser Logo sollte mit integriert werden.
Das Erscheinungsbild soll edel, elegant, markant, präsent, wieder erkennbar und einzigartig sein.
Es gibt ein paar Ideen, diese sind aber nur als Hinweise zu verstehen, die verwendet werden könnten.
Dies sind 2 Teddybären im Weinfeld, Teddybären auf einem Traktor im Weinfeld/ Weinberg, Landschaft oder eben komplett etwas anderes Kreatives.
Die Anlagen sind unser Logo in 3 Varianten und einige Beispiele von eigenen unprofessionellen Versuchen, sowie tolle Etikettendesigns die uns gefallen.
We are looking for a design for our first red wine bottle label.
The maximum height should be 130mm.
The name should be 'Bertoldo'.
The grape variety 'Cabernet Sauvignon' and the vintage 2025 should also be included.
Our logo should be integrated.
The overall look should be sophisticated, elegant, striking, memorable, recognizable, and unique.
We have a few ideas, but these are just suggestions that could be used.
These include two teddy bears in a vineyard, teddy bears on a tractor in a vineyard, a landscape, or something completely different and creative.
Attached are our logo in three variations, some examples of our own unprofessional attempts, and some great label designs that we like.
Jens & Uwe
Cal Verdunes

```html
<!DOCTYPE html>
<html lang="de">
<head>
<meta charset="utf-8">
<title>Cal Verdunes – Bertoldo Etikett</title>
<link rel="stylesheet" href="https://fonts.googleapis.com/css2?family=Montserrat:wght@500;600&family=EB+Garamond:wght@400&family=Monsieur+La+Doulaise&display=swap">
<style>
  :root {
    --backdrop: #ebe7e2;
    --label-black: #161514;
    --label-black-soft: #1f1d1b;
    --copper-dark: #8a5d38;
    --copper: #b8875a;
    --copper-light: #e3bf92;
    --ink-light: #ecebe8;
  }
  html, body {
    margin: 0;
    padding: 0;
    width: 800px;
    height: 1200px;
    overflow: hidden;
    background: var(--backdrop);
  }
  .canvas {
    position: relative;
    width: 800px;
    height: 1200px;
  }
  .label-tab {
    position: absolute;
    left: 303px;
    top: 133px;
    width: 194px;
    height: 194px;
    border-radius: 50%;
    background: var(--label-black);
    display: flex;
    align-items: center;
    justify-content: center;
  }
  .tab-ring {
    width: 150px;
    height: 150px;
    border-radius: 50%;
    border: 3px solid var(--copper);
    box-sizing: border-box;
    display: flex;
    align-items: center;
    justify-content: center;
  }
  .tab-wordmark {
    font-family: "Montserrat", sans-serif;
    font-weight: 600;
    font-size: 15px;
    letter-spacing: 0.5px;
    color: var(--copper-light);
    text-align: center;
    line-height: 1.3;
  }
  .label {
    position: absolute;
    left: 100px;
    top: 230px;
    width: 600px;
    height: 840px;
    background: radial-gradient(ellipse at 50% 40%, var(--label-black-soft), var(--label-black) 75%);
  }
  .foil-band {
    position: absolute;
    left: 0;
    top: 100px;
    width: 600px;
    height: 190px;
    background: linear-gradient(90deg, var(--copper-dark) 0%, var(--copper) 30%, var(--copper-light) 55%, var(--copper) 75%, var(--copper-dark) 100%);
  }
  .winery-name {
    position: absolute;
    top: 355px;
    width: 100%;
    text-align: center;
    font-family: "Montserrat", sans-serif;
    font-weight: 600;
    font-size: 35px;
    letter-spacing: 0.5px;
    color: var(--ink-light);
  }
  .winery-region {
    position: absolute;
    top: 407px;
    width: 100%;
    text-align: center;
    font-family: "Montserrat", sans-serif;
    font-weight: 500;
    font-size: 23px;
    letter-spacing: 2px;
    color: var(--ink-light);
  }
  .wine-name {
    position: absolute;
    top: 535px;
    width: 100%;
    text-align: center;
    font-family: "Monsieur La Doulaise", cursive;
    font-size: 110px;
    line-height: 1;
    color: var(--copper);
  }
  .wine-details {
    position: absolute;
    top: 770px;
    width: 100%;
    text-align: center;
    font-family: "EB Garamond", serif;
    font-size: 27px;
    color: var(--ink-light);
  }
</style>
</head>
<body>
  <main class="canvas">
    <div class="label">
      <div class="foil-band" role="img" aria-label="Kupferfarbenes Folienband mit gerissenen Kanten"></div>
      <div class="winery-name">CAL VERDUNES</div>
      <div class="winery-region">MALLORCA</div>
      <div class="wine-name">Bertoldo</div>
      <div class="wine-details">Cabernet Sauvignon I 2025</div>
    </div>
    <div class="label-tab">
      <div class="tab-ring">
        <div class="tab-wordmark">CAL<br>VERDUNES</div>
      </div>
    </div>
  </main>
</body>
</html>
```